Tarn - Stationary Design/Layout

We are a well established clothing design and manufacturing company (Tarn Sourcing) based in London UK, with our own factory in Bangladesh, supplying to many fashion retailers and brands. Our factory has very high environmental and ethical standards with people at its heart. Our quality of garments are second to none.
Our new logo has been proudly developed by the Pixel Guild community last month, we are now in the second phase and need the layout designed for our letterheads, double sided business cards, compliment slip and clothing ticket. Feel as creative as you like, but make sure it looks great!!
***The Logo - the logo design and colour is set and should NOT be changed and stay on a dark grey backround. The logo artwork to use is attached.
***Details to use for the business card:
Dorian Pelham
Direct Line: 020 7946 0158
dorian@tarnsourcing-example.com
Tarn Sourching Ltd.
57 - 59 Hollin Row
Fenmore . Ashcombe
NW9 4QT
Switchboard: 020 7946 0274
Fax: 020 7946 0274
www.tarnsourcing-example.co.uk
***Details to use for the letterhead and compliment slip:
Tarn Sourching Ltd.
57 - 59 Hollin Row
Fenmore . Ashcombe
NW9 4QT
Fax: 020 7946 0274
www.tarnsourcing-example.co.uk
***Details for Swing Ticket:
Size: 12cm height by 5.5cm width
One side need to have just the logo without the 'Sourcing', on the other it needs to stay blank

```html
<!DOCTYPE html>
<html lang="en">
<head>
<meta charset="utf-8">
<title>Tarn Sourcing – Business Card Layout</title>
<link rel="stylesheet" href="https://fonts.googleapis.com/css2?family=Arimo:wght@400;700&family=Questrial&display=swap">
<style>
  :root {
    --page: #ffffff;
    --label: #111111;
    --card: #262626;
    --mint: #b6e9d8;
    --text-light: #f4f4f4;
    --text-muted: #d6d6d6;
    --web: #eef2f0;
  }
  * { box-sizing: border-box; margin: 0; padding: 0; }
  html, body {
    width: 928px;
    height: 1200px;
    overflow: hidden;
    background: var(--page);
  }
  .sheet {
    position: relative;
    width: 928px;
    height: 1200px;
    font-family: "Arimo", Arial, sans-serif;
  }
  .side-label {
    position: absolute;
    left: 94px;
    font-size: 32px;
    line-height: 36px;
    color: var(--label);
    font-weight: 400;
  }
  .side-label--front { top: 44px; }
  .side-label--back { top: 612px; }

  .card {
    position: absolute;
    background: var(--card);
    overflow: hidden;
  }
  .card--front { left: 68px; top: 102px; width: 814px; height: 467px; }
  .card--back { left: 71px; top: 662px; width: 811px; height: 464px; }

  .pattern { position: absolute; display: block; }
  .card--front .pattern { left: 427px; top: 205px; width: 387px; height: 124px; }
  .card--back .pattern { left: 0; top: 0; width: 811px; height: 464px; }

  .brand-name {
    position: absolute;
    color: var(--mint);
    font-family: "Arimo", Arial, sans-serif;
    font-weight: 400;
    white-space: nowrap;
    line-height: 1;
  }
  .card--front .brand-name {
    left: 22px;
    top: 26px;
    font-size: 44px;
  }
  .card--back .brand-name {
    left: 0;
    width: 100%;
    text-align: center;
    top: 128px;
    font-size: 90px;
    letter-spacing: 1px;
  }

  .contact-person {
    position: absolute;
    left: 22px;
    top: 228px;
    color: var(--text-light);
  }
  .contact-person__name {
    font-size: 40px;
    font-weight: 700;
    line-height: 44px;
    margin-bottom: 2px;
  }
  .contact-person__line {
    font-size: 18px;
    line-height: 31px;
    color: var(--text-muted);
  }

  .company-address {
    position: absolute;
    left: 0;
    width: 100%;
    top: 358px;
    text-align: center;
    color: var(--text-muted);
    font-size: 19px;
    line-height: 31px;
    font-style: normal;
  }
  .company-address .dot { padding: 0 6px; }

  .website {
    position: absolute;
    left: 0;
    width: 100%;
    top: 386px;
    text-align: center;
    font-family: "Questrial", "Century Gothic", sans-serif;
    font-size: 32px;
    line-height: 38px;
    letter-spacing: 1px;
    color: var(--web);
  }
</style>
</head>
<body>
<main class="sheet">

  <h2 class="side-label side-label--front">Front</h2>
  <section class="card card--front">
    <svg class="pattern" role="img" aria-label="Decorative band of scattered mint squares" viewBox="0 0 387 124" preserveAspectRatio="none">
      <defs>
        <linearGradient id="front-band" x1="0" y1="0" x2="1" y2="0">
          <stop offset="0" stop-color="#b6e9d8" stop-opacity="0.1"/>
          <stop offset="0.5" stop-color="#b6e9d8" stop-opacity="0.45"/>
          <stop offset="1" stop-color="#d8f6ec" stop-opacity="0.85"/>
        </linearGradient>
      </defs>
      <rect x="0" y="0" width="387" height="124" fill="url(#front-band)"/>
    </svg>

    <div class="brand-name">Tarn Sourcing</div>

    <div class="contact-person">
      <div class="contact-person__name">Dorian Pelham</div>
      <div class="contact-person__line">Direct Line: 020 7946 0158</div>
      <div class="contact-person__line">dorian@tarnsourcing-example.com</div>
    </div>

    <address class="company-address">
      <div>Tarn Sourching Ltd.<span class="dot">•</span>57 - 59 Hollin Row</div>
      <div>Fenmore . Ashcombe<span class="dot">•</span>NW9 4QT</div>
      <div>Switchboard: 020 7946 0274<span class="dot">•</span>Fax: 020 7946 0274</div>
    </address>
  </section>

  <h2 class="side-label side-label--back">Back</h2>
  <section class="card card--back">
    <svg class="pattern" role="img" aria-label="Diagonal band of scattered translucent mint squares" viewBox="0 0 811 464" preserveAspectRatio="none">
      <defs>
        <linearGradient id="back-band" x1="0" y1="1" x2="1" y2="0">
          <stop offset="0" stop-color="#b6e9d8" stop-opacity="0.12"/>
          <stop offset="0.5" stop-color="#b6e9d8" stop-opacity="0.28"/>
          <stop offset="1" stop-color="#b6e9d8" stop-opacity="0.45"/>
        </linearGradient>
      </defs>
      <polygon points="40,464 330,464 811,210 811,0 700,0" fill="url(#back-band)"/>
    </svg>

    <div class="brand-name">Tarn Sourcing</div>

    <div class="website">www.tarnsourcing-example.co.uk</div>
  </section>

</main>
</body>
</html>
```